Website Homepage re-design Project

I run a large format poster printing business & have a website hosted on zorvacartshop using one of their templates, http://www.quelvaprints.co.uk
I am looking to update the home page to give it a more professional look, it must be clear for our clients to choose their poster type from the homepage
The design must contain the 5 poster type categories as well as most of the information above the poster categories, most of the text below the green "terms & conditions" footer can be left as it is as it's used for keywords, maybe just tidied up a bit
I would like to keep the customer reviews & sample posters on the home page along with the quick glance (fly-out) poster prices
I would also like the 4 step ordering process graphic updated, ie where it say "Select Poster Type" "Choose Poster Size" etc, there are 4 variations of this graphic which I will need to insert in their respective pages
If something can be done with the company name "Quelva Prints & Laminators" that would be great.
I would prefer a design which shows all the information down to the section where it says "Order Your Poster Here" displayed on the screen when the page is loaded
Printing

```html
<!DOCTYPE html>
<html lang="en">
<head>
<meta charset="utf-8">
<title>Quelva Prints &amp; Laminators – Poster Printing &amp; Laminating</title>
<link rel="stylesheet" href="https://fonts.googleapis.com/css2?family=Ubuntu:wght@400;500;700&family=Oswald:wght@500&family=Cinzel:wght@600&family=Roboto+Slab:wght@400;500&family=Open+Sans:wght@400;600&display=swap">
<style>
:root{
  --orange:#f39a1f;
  --orange-dark:#e8730c;
  --navy:#1b3c78;
  --blue:#1f66b3;
  --green:#4a9a2a;
  --red:#d8331c;
  --ink:#222;
  --body:#555;
  --muted:#9aa3a8;
  --line:#d9e1e5;
  --sky:#d9f5fb;
  --white:#fff;
}
*{box-sizing:border-box;margin:0;padding:0}
html,body{width:1200px;height:2212px;overflow:hidden}
body{font-family:"Open Sans",Arial,sans-serif;color:var(--ink);
  background:linear-gradient(90deg,var(--sky) 0%,#f3fcfe 18%,#fff 35%,#fff 65%,#f3fcfe 82%,var(--sky) 100%)}
.page{position:relative;width:1200px;height:2212px}
.abs{position:absolute}

/* top bar */
.topbar{position:absolute;left:0;top:0;width:1200px;height:32px;background:var(--orange);color:#fff;
  font:500 11px "Ubuntu",sans-serif;display:flex;align-items:center;justify-content:space-between;padding:0 140px;letter-spacing:.3px}
.topbar nav{display:flex;gap:52px}

/* header */
.brand{position:absolute;left:140px;top:58px;display:flex;align-items:center;gap:12px}
.brand-mark{width:62px;height:62px;background:var(--orange)}
.brand-name{font:700 21px "Ubuntu",sans-serif;color:var(--navy);width:190px;line-height:1.15}
.currency{position:absolute;left:710px;top:66px;font:600 8px "Open Sans",sans-serif;color:#333}
.currency .flags{display:flex;gap:4px;margin-top:4px}
.flag{width:17px;height:11px}
.search{position:absolute;left:812px;top:70px;width:248px;height:26px;border:1px solid #bbb;background:#fff;display:flex}
.search span{flex:1;font-size:10px;color:#999;padding:6px 8px}
.search b{background:#333;color:#fff;font:600 10px "Open Sans",sans-serif;padding:6px 8px}
.mainnav{position:absolute;left:485px;top:126px;display:flex;gap:38px;font:500 15.5px "Ubuntu",sans-serif;color:#111}
.mainnav .active{color:var(--orange-dark)}
.mainnav .cart{color:var(--orange-dark);display:flex;gap:6px;align-items:center}

/* hero */
.hero{position:absolute;left:140px;top:160px;width:920px;height:369px;border-radius:6px;overflow:hidden;
  background:linear-gradient(90deg,#f4f4f4 0%,#fafafa 45%,#eeeeee 100%)}
.hero-photo{position:absolute;left:0;top:0;width:520px;height:369px;background:linear-gradient(120deg,#e9e9e9,#d8d8d8 60%,#f3f3f3)}
.hero h1{position:absolute;left:332px;top:50px;font:500 35px "Ubuntu",sans-serif;color:var(--red);letter-spacing:.3px}
.hero p{position:absolute;left:334px;top:98px;font:500 17.5px "Ubuntu",sans-serif;color:#333}
.hero .cta{position:absolute;left:598px;top:208px;width:212px;height:58px;border-radius:8px;background:linear-gradient(#3b3f50,#1c1f2b);
  border:3px solid #dfe0e4;color:#fff;font:700 20px "Oswald",sans-serif;display:flex;align-items:center;justify-content:center;letter-spacing:.5px}
.dots{position:absolute;left:774px;top:322px;display:flex;gap:9px}
.dots i{width:17px;height:17px;border-radius:50%;background:#fff;border:2px solid #ccc}
.dots i:first-child{background:var(--blue);border-color:#fff;box-shadow:0 0 0 1px #bbb}

/* order banner */
.order-tag{position:absolute;left:140px;top:556px;height:36px;padding:0 18px 0 6px;background:var(--red);color:#fff;
  font:500 27px "Oswald",sans-serif;line-height:36px;letter-spacing:.5px;text-transform:uppercase}
.order-sub{position:absolute;left:585px;top:558px;font:600 21px "Cinzel",serif;color:var(--green)}
.delivery{position:absolute;left:140px;top:605px;width:920px;font:600 15px "Open Sans",sans-serif;color:#111;line-height:1.45}
.rule{position:absolute;left:140px;width:920px;height:1px;background:var(--line)}

/* panels */
.panel{position:absolute;left:140px;width:920px;background:#fff;border:1px solid #e3e8ea;border-radius:6px;box-shadow:0 2px 6px rgba(0,0,0,.05)}
.cat{position:absolute;width:270px}
.cat h3{font:500 16.5px "Ubuntu",sans-serif;color:var(--orange-dark);padding-bottom:8px;border-bottom:1px solid var(--line);margin-bottom:8px}
.cat p{font-size:10px;line-height:1.5;color:var(--body)}
.cat.centre{width:260px}
.cat.centre h3{border-bottom:0;padding-bottom:10px}
.swatch-pic{position:absolute;left:475px;top:686px;width:262px;height:106px;border-radius:3px;
  background:linear-gradient(90deg,#5e4a42,#f08a3a 35%,#d9cf3a 50%,#e85a5a 62%,#3f4a58 100%)}

.prices-tag{position:absolute;left:134px;top:992px;height:33px;padding:0 22px 0 10px;background:var(--blue);color:#fff;
  font:500 26px "Oswald",sans-serif;line-height:33px;text-transform:uppercase;clip-path:polygon(0 0,94% 0,100% 50%,94% 100%,0 100%)}
.step{position:absolute;width:200px;text-align:center}
.step h4{font:500 27px "Roboto Slab",serif;color:#d6dadd}
.step small{display:block;font:500 15px "Roboto Slab",serif;color:#d6dadd;margin-top:-2px}
.step.active h4{color:var(--green)}
.step.active small{color:#111}

.info h2{position:absolute;left:168px;top:1280px;font:400 27px "Open Sans",sans-serif;color:var(--blue)}
.info .lead{position:absolute;left:168px;top:1322px;width:860px;font:400 16px "Open Sans",sans-serif;line-height:1.6;color:#111}
.info .note{position:absolute;left:168px;top:1391px;width:860px;font-size:11px;line-height:1.6;color:#777}
.info .claim{position:absolute;left:168px;top:1442px;font:600 16px "Open Sans",sans-serif;color:var(--green)}

/* samples & reviews */
.section-title{position:absolute;font:500 19px "Roboto Slab",serif;color:#111}
.sample-label{position:absolute;font:400 14px "Roboto Slab",serif;color:#111}
.frame{position:absolute;width:137px;height:259px;background:#fff;border:1px solid #ccc;box-shadow:0 1px 4px rgba(0,0,0,.25);padding:8px}
.frame div{width:100%;height:100%}
.divider{position:absolute;left:614px;top:1526px;width:1px;height:340px;background:var(--line)}
.reviews{position:absolute;left:660px;top:1557px;width:400px;border-top:1px solid var(--line);padding-top:10px;font-size:10.5px;line-height:1.55;color:#666}
.reviews p{margin-bottom:10px}
.stars{display:flex;gap:1px;margin:4px 0 2px}
.reviewer{font-style:italic;color:var(--green);margin-bottom:26px}

/* footer */
.footer-line{position:absolute;left:140px;width:920px;border-top:1px dashed #ccd5d8}
.fcol{position:absolute;top:1972px;font-size:10px;line-height:1.9;color:#333}
.fcol h5{font:700 10px "Roboto Slab",serif;color:var(--orange-dark);text-transform:uppercase;margin-bottom:16px;letter-spacing:.3px}
.vsep{position:absolute;top:1930px;height:170px;border-left:1px dashed #ccd5d8}
.copy{position:absolute;right:140px;top:2131px;font-size:10px;color:#333}
.foot-brand{position:absolute;left:148px;top:2134px;display:flex;align-items:center;gap:8px}
.foot-brand i{width:32px;height:32px;background:#b9bfc3}
.foot-brand span{font:500 11px "Ubuntu",sans-serif;color:#8c9499;width:110px;line-height:1.2}
.social{position:absolute;left:964px;top:2152px;display:flex;gap:6px}
.social i{width:28px;height:28px;border-radius:5px;background:#3b5f9e}
.social i:nth-child(2){background:#3aa8e0}
.social i:nth-child(3){background:#2f7fd0}
</style>
</head>
<body>
<div class="page">

  <header>
    <div class="topbar">
      <span>TEL: 01632 960481 &nbsp;|&nbsp; MOB: 07700 900 417</span>
      <nav><span>LOGIN</span><span>CONTACT</span><span>FAQ'S</span></nav>
    </div>
    <div class="brand"><i class="brand-mark"></i><span class="brand-name">Quelva Prints &amp; Laminators</span></div>
    <div class="currency">SELECT CURRENCY
      <div class="flags">
        <i class="flag" style="background:#1d3f9a"></i><i class="flag" style="background:#c8202f"></i><i class="flag" style="background:linear-gradient(#c8202f 50%,#fff 50%)"></i>
      </div>
    </div>
    <div class="search"><span>Enter your search ...</span><b>SEARCH ⌕</b></div>
    <nav class="mainnav">
      <span class="active">Home</span><span>About Us</span><span>Colour Calibration</span><span>Customer Comments</span>
      <span class="cart"><svg width="17" height="15" viewBox="0 0 17 15"><path d="M1 1h3l2 9h8l2-6H5" fill="none" stroke="#555" stroke-width="1.6"/><circle cx="7" cy="13" r="1.4" fill="#555"/><circle cx="13" cy="13" r="1.4" fill="#555"/></svg>View Cart</span>
    </nav>
  </header>

  <section class="hero">
    <div class="hero-photo" role="img" aria-label="Photo of a smiling woman collecting a print from a desktop photo printer"></div>
    <h1>POSTER PRINTING &amp; LAMINATING</h1>
    <p>Order below in 4 simple steps &amp; receive your poster the Next Day</p>
    <div class="cta">GET POSTER PRICES</div>
    <div class="dots"><i></i><i></i><i></i><i></i><i></i></div>
  </section>

  <div class="order-tag">Order your poster here</div>
  <svg class="abs" style="left:520px;top:550px" width="66" height="40" viewBox="0 0 66 40"><path d="M2 20 Q30 2 56 18" fill="none" stroke="#bbb" stroke-width="3"/><path d="M50 9 L62 20 L48 26" fill="none" stroke="#bbb" stroke-width="3"/></svg>
  <div class="order-sub">Select Your Poster Type Below &amp; Upload Your File.</div>
  <p class="delivery">Orders placed before 2pm are sent out the same day with either standard delivery @£4.50+vat or Swiftline next day delivery @ £9.50+vat to anywhere in the UK</p>
  <div class="rule" style="top:654px"></div>

  <section class="panel" style="top:667px;height:297px">
  </section>
  <div class="cat" style="left:170px;top:690px"><h3>Matt Photo Paper</h3><p>Photo Quality Poster printing, Printed at 2400 dpi on 180gsm Silk Matt Photo paper, perfect for high quality presentations &amp; matt photo reproduction, these poster will show the finest details</p></div>
  <div class="cat" style="left:170px;top:806px"><h3>Student Presentation Poster</h3><p>Photo Quality Poster Printing, Printed at 1200dpi on 170gsm High Resolution coated paper, this printing option is ideally suited to students presentations</p></div>
  <div class="swatch-pic" role="img" aria-label="Fanned stack of printed photos and colour paper samples"></div>
  <div class="cat centre" style="left:477px;top:806px"><h3>Poster with Gloss Encapsulating</h3><p>Photo Quality Poster printing &amp; Laminating. Printed at 2400 dpi &amp; Laminated on both sides with a 5mm edge seal, the Gloss finish enhances the colours. Weatherproof &amp; durable, these posters are ideal for long term use</p></div>
  <div class="cat" style="left:774px;top:690px"><h3>Gloss Photo Paper</h3><p>Photo Quality Poster Printing, Printed at 2400 dpi on 190gsm Gloss Photo paper, perfect for high quality presentations &amp; photographic prints with vivid true to life colours.</p></div>
  <div class="cat" style="left:774px;top:806px"><h3>Poster with Matt Encapsulating</h3><p>Photo Quality Poster printing &amp; Laminating. Printed at 2400dpi &amp; Laminated on both sides with a 5mm edge seal, the Matt finish reduces light reflection. Weatherproof &amp; durable, these posters are ideal for long term use</p></div>

  <section class="panel" style="top:1000px;height:502px"></section>
  <div class="prices-tag">Poster prices</div>

  <svg class="abs" style="left:160px;top:1105px" width="880" height="104" viewBox="0 0 880 104">
    <g fill="none" stroke="#d0d5d8" stroke-width="1.5" stroke-dasharray="4 4">
      <line x1="10" y1="51" x2="860" y2="51"/>
    </g>
    <g fill="none" stroke="#ccd1d4" stroke-width="1.5">
      <path d="M150 41l10 10-10 10M162 41l10 10-10 10"/><path d="M380 41l10 10-10 10M392 41l10 10-10 10"/><path d="M612 41l10 10-10 10M624 41l10 10-10 10"/><path d="M844 41l10 10-10 10M856 41l10 10-10 10"/>
    </g>
    <!-- step 1 -->
    <circle cx="76" cy="51" r="44" fill="#efe6d3" stroke="#d8cba9" stroke-width="3"/>
    <rect x="56" y="33" width="36" height="36" fill="#fff" stroke="#4a9a2a" stroke-width="3"/>
    <path d="M60 50l12 12 24-30" fill="none" stroke="#4a9a2a" stroke-width="6"/>
    <circle cx="118" cy="84" r="17" fill="#4a9a2a" stroke="#fff" stroke-width="3"/>
    <text x="118" y="90" font-family="Open Sans,sans-serif" font-size="15" fill="#fff" text-anchor="middle">1</text>
    <!-- step 2 -->
    <circle cx="301" cy="51" r="44" fill="#f1f2f3" stroke="#e1e3e5" stroke-width="3"/>
    <path d="M283 51a18 18 0 0 1 32-11M319 51a18 18 0 0 1-32 11" fill="none" stroke="#d2d5d8" stroke-width="5"/>
    <circle cx="343" cy="84" r="17" fill="#c8cbce" stroke="#fff" stroke-width="3"/>
    <text x="343" y="90" font-family="Open Sans,sans-serif" font-size="15" fill="#fff" text-anchor="middle">2</text>
    <!-- step 3 -->
    <circle cx="531" cy="51" r="44" fill="#f1f2f3" stroke="#e1e3e5" stroke-width="3"/>
    <circle cx="531" cy="51" r="20" fill="none" stroke="#d2d5d8" stroke-width="4"/>
    <path d="M531 63V41M521 50l10-10 10 10" fill="none" stroke="#d2d5d8" stroke-width="5"/>
    <circle cx="573" cy="84" r="17" fill="#c8cbce" stroke="#fff" stroke-width="3"/>
    <text x="573" y="90" font-family="Open Sans,sans-serif" font-size="15" fill="#fff" text-anchor="middle">3</text>
    <!-- step 4 -->
    <circle cx="771" cy="51" r="44" fill="#f1f2f3" stroke="#e1e3e5" stroke-width="3"/>
    <path d="M760 34h16v8M760 34v34h16v-8M768 51h20M782 44l7 7-7 7" fill="none" stroke="#d2d5d8" stroke-width="4"/>
    <circle cx="813" cy="84" r="17" fill="#c8cbce" stroke="#fff" stroke-width="3"/>
    <text x="813" y="90" font-family="Open Sans,sans-serif" font-size="15" fill="#fff" text-anchor="middle">4</text>
  </svg>
  <div class="step active" style="left:137px;top:1048px"><h4>Select</h4><small>Poster Type</small></div>
  <div class="step" style="left:362px;top:1048px"><h4>Choose</h4><small>Poster Size</small></div>
  <div class="step" style="left:592px;top:1048px"><h4>Upload</h4><small>Your File</small></div>
  <div class="step" style="left:832px;top:1048px"><h4>Checkout</h4><small>Pay for your Poster</small></div>

  <section class="info">
    <h2>Large Format Full Colour Photographic &amp; Presentation Quality Posters</h2>
    <p class="lead">Poster printing at 2400dpi on the highest Quality 190gsm Photo Papers using the latest Vantor V6100 Photo Printers with 8 COLOUR PIGMENT Inks* producing Millions of vibrant colours that will not fade over time.</p>
    <p class="note">*(unlike dye based inks which will start to fade in a matter of days in direct daylight) or cheap Dry Toner posters which are printed on low quality 90GSM paper with only 4 colours &amp; therefore unable to produce the same quality &amp; detail as poster printing on 8 colour Photo Printers.</p>
    <p class="claim">Photo quality prints that simply cannot be matched by any 4 colour printing process.</p>
  </section>

  <section class="samples">
    <h3 class="section-title" style="left:140px;top:1528px">Our Sample Posters</h3>
    <span class="sample-label" style="left:149px;top:1572px">Menu Posters</span>
    <span class="sample-label" style="left:374px;top:1572px">Scientific Posters</span>
    <div class="frame" style="left:151px;top:1596px"><div role="img" aria-label="Sample menu poster with curry dishes on a red background" style="background:linear-gradient(160deg,#c4173a,#9b0f2c 60%,#7a0a24)"></div></div>
    <div class="frame" style="left:378px;top:1596px"><div role="img" aria-label="Sample scientific research poster with text columns and charts" style="background:linear-gradient(#3d7cc4 0 8%,#e8eef5 8%)"></div></div>
  </section>
  <div class="divider"></div>

  <section>
    <h3 class="section-title" style="left:660px;top:1526px">Customer Reviews</h3>
    <div class="reviews">
      <p>The posters arrived today and are perfect. Your service has been flawless in all regards.</p>
      <p>Helpful, prompt less than 24 hour turnaround, and the quality is excellent. I am very particular about the print quality of my work and have not seen better. You are now on file as the preferred printer for our company.</p>
      <div class="stars"><svg width="56" height="10" viewBox="0 0 56 10" fill="#f2b705" stroke="#c98a00" stroke-width=".5"><g id="st"><path d="M5 0l1.5 3.3 3.5.3-2.7 2.3.9 3.5L5 7.5 1.8 9.4l.9-3.5L0 3.6l3.5-.3z"/></g><use href="#st" x="11"/><use href="#st" x="22"/><use href="#st" x="33"/><use href="#st" x="44"/></svg></div>
      <p class="reviewer">- Owen Marlowe (from Dunfield)</p>
      <p>Gareth, Thanks very much for a very swift turnaround time and the final product is fantastic. I will definitely be recommending you and will be using you again.</p>
      <div class="stars"><svg width="56" height="10" viewBox="0 0 56 10" fill="#f2b705" stroke="#c98a00" stroke-width=".5"><use href="#st"/><use href="#st" x="11"/><use href="#st" x="22"/><use href="#st" x="33"/><use href="#st" x="44"/></svg></div>
      <p class="reviewer">- Peter Halden</p>
    </div>
  </section>

  <footer>
    <div class="footer-line" style="top:1926px"></div>
    <div class="fcol" style="left:142px"><h5>About Us</h5>Home<br>About Us<br>View Cart<br>Colour Calibration</div>
    <div class="vsep" style="left:290px"></div>
    <div class="fcol" style="left:352px"><h5>Support</h5>Client Login<br>Contact Us<br>FAQ's<br>Customer Comments</div>
    <div class="vsep" style="left:526px"></div>
    <div class="fcol" style="left:581px"><h5>Legal Info</h5>Terms of Use<br>Privacy Policy<br>Copyright Policy</div>
    <div class="vsep" style="left:720px"></div>
    <div class="fcol" style="left:780px"><h5>Quelva Prints &amp; Laminators</h5>Nant Y Garn, Heol Fawr<br>Pentrebryn<br>Llanfelin<br>SA99 1ZZ</div>
    <div class="fcol" style="left:945px;top:2007px">Tel: 01632 960481<br>Mob: 07700 900 417<br>Fax: 01632 960482<br>hello@quelvaprints.co.uk</div>
    <div class="footer-line" style="top:2110px;border-top-style:solid"></div>
    <div class="foot-brand"><i></i><span>Quelva Prints &amp; Laminators</span></div>
    <p class="copy">© 2012 Quelva Prints &amp; Laminators. All Rights Reserved.</p>
    <div class="social"><i></i><i></i><i></i></div>
  </footer>

</div>
</body>
</html>
```